Online interactive calendar for training organisation

We have a new website being made and need a design for an online calendar that is interactive and very simple and easy to use. On our main page this calendar will include all of our courses (approx 30 different ones with up to 8 different locations). On our sub pages which have course information, the calendar will only include details of that specific course. Details needed are: Course code, course name/title, date, duration (1/2 day - 5 days), location, price, discount price. Maybe also a key for available or limited spots left? We want a section at the top of the calendar to be able to filter by location or course, and maybe to filter by month also? I have included a spreadsheet with a sample of our courses with this information. Also a sample draft of the main page on our new webpage to show the colour green which is our company colour. Main notes - we want as simple, effective and easy to use as possible.
We will need to know what plug in we can use to get the design you have created.

Target Market(s)

Mining and construction - both companies and individuals

Number of Pages Required

1 page

Colors
cadf82

Requirements
Must have
• Be simple, easy to use, effective.

```html
<!DOCTYPE html>
<html lang="en">
<head>
<meta charset="utf-8">
<title>Course Calendar – November 2019</title>
<link rel="stylesheet" href="https://fonts.googleapis.com/css2?family=Outfit:wght@300;400;500&display=swap">
<style>
  :root {
    --brand-green: #cadf82;
    --ink: #111111;
    --muted: #9b9b9b;
    --bar-grey: #f1f1f1;
    --card-bg: #ffffff;
    --page-bg: #ffffff;
    --card-edge: #9a9a9a;
  }
  * { box-sizing: border-box; margin: 0; padding: 0; }
  html, body {
    width: 1200px; height: 809px; overflow: hidden;
    background: var(--page-bg);
    font-family: "Outfit", sans-serif;
    color: var(--ink);
  }
  .calendar-card {
    position: absolute; left: 32px; top: 40px;
    width: 1135px; height: 727px;
    background: var(--card-bg);
    border: 1px solid var(--card-edge);
    border-radius: 52px;
    box-shadow: 4px 8px 14px rgba(0,0,0,0.28);
  }
  .month-nav {
    position: absolute; left: 0; top: 54px; width: 1135px; height: 44px;
  }
  .month-title {
    position: absolute; left: 595px; top: 4px; transform: translateX(-50%);
    font-size: 33px; font-weight: 500; letter-spacing: -0.3px; white-space: nowrap;
  }
  .nav-arrow { position: absolute; top: 10px; width: 18px; height: 26px; }
  .nav-arrow.prev { left: 445px; }
  .nav-arrow.next { left: 728px; }
  .filter-button { position: absolute; left: 988px; top: 64px; width: 28px; height: 28px; }

  .weekday-bar {
    position: absolute; left: 122px; top: 122px; width: 892px; height: 31px;
    background: var(--bar-grey); border-radius: 16px;
    display: grid; grid-template-columns: repeat(7, 1fr); align-items: center;
  }
  .weekday { text-align: center; font-size: 19px; font-weight: 400; letter-spacing: 0.5px; color: var(--brand-green); }
  .weekday.weekend { color: var(--ink); }

  .day-grid {
    position: absolute; left: 122px; top: 165px; width: 892px;
    display: grid; grid-template-columns: repeat(7, 1fr); grid-auto-rows: 101.5px;
  }
  .day-number { text-align: right; padding-right: 11px; font-size: 19px; font-weight: 300; line-height: 24px; }
  .day-number.other-month { color: var(--muted); }

  .course-event {
    position: absolute; height: 17px;
    background: var(--brand-green);
    font-size: 11.5px; font-weight: 400; line-height: 17px;
    text-align: center; white-space: nowrap;
  }
  .course-event::before, .course-event::after {
    content: ""; position: absolute; top: 0; width: 17px; height: 17px; border-radius: 50%;
    background: #fff;
  }
  .course-event::before {
    left: -4px;
    background: radial-gradient(circle, var(--brand-green) 0 4.5px, #fff 5px);
    box-shadow: 0 0 0 0.5px rgba(0,0,0,0.08);
  }
  .course-event::after { right: -8px; box-shadow: 0 0 0 0.5px rgba(0,0,0,0.08); }
  .course-event .label { position: relative; }

  .event-work-safety { left: 381px; top: 190px; width: 123px; padding-left: 14px; text-align: left; }
  .event-forklift { left: 509px; top: 190px; width: 378px; }
  .event-scaffolding { left: 253px; top: 292px; width: 634px; }
  .event-first-aid { left: 760px; top: 393px; width: 61px; padding-left: 4px; }
</style>
</head>
<body>
<main class="calendar-card">
  <header class="month-nav">
    <svg class="nav-arrow prev" viewBox="0 0 18 26" aria-label="Previous month"><path d="M14 2 L4 13 L14 24" fill="none" stroke="#111" stroke-width="3.2" stroke-linecap="round" stroke-linejoin="round"/></svg>
    <h1 class="month-title">November 2019</h1>
    <svg class="nav-arrow next" viewBox="0 0 18 26" aria-label="Next month"><path d="M4 2 L14 13 L4 24" fill="none" stroke="#111" stroke-width="3.2" stroke-linecap="round" stroke-linejoin="round"/></svg>
  </header>
  <svg class="filter-button" viewBox="0 0 28 28" aria-label="Filter courses"><path d="M1 1 H27 L17 13 V27 L12 22 V13 Z" fill="#cadf82"/></svg>

  <div class="weekday-bar">
    <span class="weekday weekend">SUN</span><span class="weekday">MON</span><span class="weekday">TUE</span><span class="weekday">WED</span><span class="weekday">THU</span><span class="weekday">FRI</span><span class="weekday weekend">SAT</span>
  </div>

  <div class="day-grid">
    <span class="day-number other-month">27</span><span class="day-number other-month">28</span><span class="day-number other-month">29</span><span class="day-number other-month">30</span><span class="day-number other-month">31</span><span class="day-number">1</span><span class="day-number">2</span>
    <span class="day-number">3</span><span class="day-number">4</span><span class="day-number">5</span><span class="day-number">6</span><span class="day-number">7</span><span class="day-number">8</span><span class="day-number">9</span>
    <span class="day-number">10</span><span class="day-number">11</span><span class="day-number">12</span><span class="day-number">13</span><span class="day-number">14</span><span class="day-number">15</span><span class="day-number">16</span>
    <span class="day-number">17</span><span class="day-number">18</span><span class="day-number">19</span><span class="day-number">20</span><span class="day-number">21</span><span class="day-number">22</span><span class="day-number">23</span>
    <span class="day-number">24</span><span class="day-number">25</span><span class="day-number">26</span><span class="day-number">27</span><span class="day-number">28</span><span class="day-number">29</span><span class="day-number">30</span>
  </div>

  <div class="course-event event-work-safety"><span class="label">Work Safety at...</span></div>
  <div class="course-event event-forklift"><span class="label">Forklift</span></div>
  <div class="course-event event-scaffolding"><span class="label">Basic Scaffolding</span></div>
  <div class="course-event event-first-aid"><span class="label">FA</span></div>
</main>
</body>
</html>
```